Design an attractive wine label for Brell Fine Wines

we need a wine label design, we are an Australian wine exporting company'Brell Fine Wines'. We succeed several pallets in last few months and is going to launch our first container. So it’s time to start our own brands. we will have some wines display in China's shopping mall shelves, so we want to have a catchy label which can attract Chinese eyes immediately. other details you will see in the file i uploaded. The design should include a front and back label.

Target Market(s)

Brell Fine Wines are targeting middle class wine drinkers in 2nd-4th tier Chinese cities.

Colors

Designer to choose colors to be used in the design.

Requirements
Must have
• We’d like something that at first glance is Australian (element, style or color…) but subconsciously connects to the Chinese. Demeanor bearing in mind the demographics targeted across the ranges. We would expect the designs and naming to becoming more formalized as they rise to platinum.
Nice to have
• creative things come out
Should not have
• any dead related word or icon, no number '4' related word or icon, no skull related word or icon, kangaroo (see brand 'Copper vine')

```html
<!DOCTYPE html>
<html lang="en">
<head>
<meta charset="utf-8">
<title>Wirrana Platinum Edition – Front Label</title>
<link rel="stylesheet" href="https://fonts.googleapis.com/css2?family=EB+Garamond:wght@400;500&family=Anton&display=swap">
<style>
  :root {
    --page: #ffffff;
    --charcoal: #373737;
    --silver: #9a9a9a;
    --ink: #1e1e1e;
    --wine-red: #b22129;
    --white: #ffffff;
    --vine-light: #a4a4a4;
    --vine-dark: #6e6e6e;
    --caption: #000000;
  }
  * { margin: 0; padding: 0; box-sizing: border-box; }
  html, body {
    width: 1200px;
    height: 1200px;
    overflow: hidden;
    background: var(--page);
  }
  .canvas {
    position: relative;
    width: 1200px;
    height: 1200px;
  }
  .label {
    position: absolute;
    left: 321px;
    top: 70px;
    width: 558px;
    height: 1004px;
    display: flex;
    flex-direction: column;
    font-family: "EB Garamond", "Times New Roman", serif;
  }
  .label__crest-panel {
    position: relative;
    height: 473px;
    background: var(--charcoal);
  }
  .label__vine-art {
    position: absolute;
    left: 172px;
    top: 163px;
    width: 225px;
    height: 248px;
    border-radius: 40% 50% 45% 55%;
    background: radial-gradient(ellipse at 55% 45%, var(--vine-light), var(--vine-dark) 70%, var(--charcoal));
    opacity: 0.85;
  }
  .label__brand-band {
    height: 93px;
    background: var(--silver);
    text-align: center;
    padding-top: 8px;
  }
  .brand-name {
    font-size: 54px;
    font-weight: 400;
    letter-spacing: 2px;
    line-height: 1;
    color: var(--white);
    text-shadow: 1px 1px 2px rgba(0,0,0,0.55);
  }
  .brand-edition {
    font-size: 18px;
    color: var(--ink);
    line-height: 1.1;
    margin-top: 2px;
  }
  .label__rule {
    background: var(--ink);
  }
  .label__rule--upper { height: 14px; }
  .label__rule--lower { height: 12px; }
  .label__variety-band {
    height: 69px;
    background: var(--wine-red);
    color: var(--white);
    text-align: center;
    padding-top: 8px;
  }
  .variety {
    font-size: 27px;
    line-height: 1.05;
  }
  .vintage {
    font-size: 18px;
    line-height: 1;
  }
  .label__producer-panel {
    flex: 1;
    background: var(--wine-red);
    color: var(--white);
    text-align: center;
    display: flex;
    flex-direction: column;
    justify-content: flex-end;
    padding-bottom: 36px;
  }
  .producer {
    font-size: 27px;
    line-height: 1.1;
  }
  .region {
    font-size: 18px;
    line-height: 1.1;
  }
  .range-caption {
    position: absolute;
    left: 321px;
    top: 1094px;
    width: 558px;
    text-align: center;
    font-family: "Anton", "Impact", sans-serif;
    font-size: 38px;
    letter-spacing: 0.5px;
    color: var(--caption);
  }
</style>
</head>
<body>
  <main class="canvas">
    <section class="label">
      <div class="label__crest-panel">
        <div class="label__vine-art" role="img" aria-label="Embossed silver grapevine with leaves and a bunch of grapes"></div>
      </div>
      <div class="label__brand-band">
        <h1 class="brand-name">WIRRANA</h1>
        <p class="brand-edition">Platinum Edition</p>
      </div>
      <div class="label__rule label__rule--upper"></div>
      <div class="label__variety-band">
        <p class="variety">Cabernet Sauvignon</p>
        <p class="vintage">Vintage 2010</p>
      </div>
      <div class="label__rule label__rule--lower"></div>
      <div class="label__producer-panel">
        <p class="producer">Brell Fine Wines</p>
        <p class="region">Western Australia</p>
      </div>
    </section>
    <p class="range-caption">PLATINUM RED</p>
  </main>
</body>
</html>
```